Marlo Vista Table & Chair Rentals

We need a business card for a table and chair rental company. We rent tables and chairs for weddings, funerals, business events and parties. We want something that looks clean and elegant while not being too busy. We would like colors in the green and blue hues and avoiding anything orange. We want to make sure the font is large enough to be seen easily.

Target Market(s)

Wedding & Event Rentals

Industry/Entity Type

Events

Contact Information for Business Card

Marlo Vista, sales@marlovistarentals.example, marlovistarentals.example, 360-555-0182

Requirements
Must have
• Easy to read font
Should not have
• Orange anywhere in the design

```html
<!DOCTYPE html>
<html lang="en">
<head>
<meta charset="utf-8">
<title>Marlo Vista Table &amp; Chair Rentals – Business Card</title>
<link rel="stylesheet" href="https://fonts.googleapis.com/css2?family=Merriweather:wght@700&family=Open+Sans:wght@400&display=swap">
<style>
  :root {
    --ink-blue: #3e6587;
    --sea-teal: #78aaae;
    --mid-stripe: #5b8ba5;
    --pale-teal: #84b6b9;
    --canvas-bg: #eceae6;
    --divider: #5f8c9c;
  }
  * { box-sizing: border-box; margin: 0; padding: 0; }
  html, body {
    width: 1200px; height: 1000px; overflow: hidden;
    background: var(--canvas-bg);
  }
  .stage {
    position: relative; width: 1200px; height: 1000px;
    display: flex; flex-direction: column; align-items: center; justify-content: center; gap: 50px;
  }
  .card {
    position: relative; width: 720px; height: 411px; overflow: hidden;
    box-shadow: 0 6px 18px rgba(0,0,0,.18);
  }

  /* ---- Back of card ---- */
  .card--back { background: var(--ink-blue); }
  .back-brand {
    position: absolute; left: 0; right: 0; top: 110px; text-align: center;
    font-family: "Merriweather", Georgia, serif; font-weight: 700;
    font-size: 42px; color: var(--pale-teal); letter-spacing: .5px;
  }
  .back-rule {
    position: absolute; height: 9px; background: var(--sea-teal);
  }
  .back-rule--right { top: 200px; left: 440px; right: 0; }
  .back-rule--left { top: 282px; left: 0; width: 430px; }
  .back-web {
    position: absolute; top: 270px; left: 445px;
    font-family: "Open Sans", Arial, sans-serif; font-size: 19px; color: var(--pale-teal);
  }
  .back-edge {
    position: absolute; left: 0; right: 0; bottom: 0; height: 14px; background: var(--sea-teal);
  }

  /* ---- Front of card ---- */
  .card--front { background: var(--ink-blue); }
  .front-upper {
    position: absolute; left: 0; right: 0; top: 0; height: 232px; background: var(--sea-teal);
  }
  .front-stripe {
    position: absolute; left: 0; right: 0; top: 232px; height: 10px; background: var(--mid-stripe);
  }
  .front-mark {
    position: absolute; left: 90px; top: 90px;
    display: flex; align-items: center; gap: 12px;
  }
  .front-mark__dot {
    width: 22px; height: 22px; border-radius: 50%; background: var(--ink-blue);
  }
  .front-mark__name {
    font-family: "Merriweather", Georgia, serif; font-weight: 700;
    font-size: 30px; color: var(--ink-blue);
  }
  .front-divider {
    position: absolute; left: 352px; top: 32px; width: 1px; height: 160px; background: var(--divider);
  }
  .services {
    position: absolute; left: 378px; top: 46px;
    font-family: "Open Sans", Arial, sans-serif; font-size: 19px; line-height: 1.3;
    color: var(--ink-blue); list-style: none;
  }
  .services li.indent { padding-left: 22px; }

  .identity {
    position: absolute; right: 335px; top: 282px; text-align: right;
    font-family: "Merriweather", Georgia, serif; font-weight: 700;
    color: var(--pale-teal); font-size: 26px; line-height: 1.25;
  }
  .identity__person { font-size: 30px; }
  .contact-divider {
    position: absolute; left: 400px; top: 280px; width: 1px; height: 64px; background: var(--divider);
  }
  .contact {
    position: absolute; left: 414px; top: 280px; list-style: none;
    font-family: "Open Sans", Arial, sans-serif; font-size: 17px; color: var(--pale-teal);
  }
  .contact li { display: flex; align-items: center; gap: 8px; height: 32px; }
  .contact svg { width: 20px; height: 20px; flex: none; }
</style>
</head>
<body>
<main class="stage">

  <section class="card card--back" aria-label="Business card back">
    <div class="back-brand">Marlo Vista</div>
    <div class="back-rule back-rule--right"></div>
    <div class="back-rule back-rule--left"></div>
    <div class="back-web">marlovistarentals.example</div>
    <div class="back-edge"></div>
  </section>

  <section class="card card--front" aria-label="Business card front">
    <div class="front-upper"></div>
    <div class="front-stripe"></div>

    <div class="front-mark">
      <span class="front-mark__dot"></span>
      <span class="front-mark__name">Marlo Vista</span>
    </div>
    <div class="front-divider"></div>
    <ul class="services">
      <li>We rent tables and chairs for</li>
      <li class="indent">weddings,</li>
      <li class="indent">funerals,</li>
      <li class="indent">business events and parties</li>
    </ul>

    <div class="identity">
      <div class="identity__company">Marlo Vista</div>
      <div class="identity__person">Your Name here</div>
    </div>
    <div class="contact-divider"></div>
    <ul class="contact">
      <li>
        <svg viewBox="0 0 20 20" aria-hidden="true">
          <circle cx="10" cy="10" r="10" fill="var(--pale-teal)"/>
          <rect x="7" y="4.5" width="6" height="11" rx="1.2" fill="var(--ink-blue)"/>
          <rect x="8" y="6" width="4" height="7" fill="var(--pale-teal)"/>
        </svg>
        <span>360-555-0182</span>
      </li>
      <li>
        <svg viewBox="0 0 20 20" aria-hidden="true">
          <circle cx="10" cy="10" r="10" fill="var(--pale-teal)"/>
          <rect x="5" y="6.5" width="10" height="7" rx="1" fill="var(--ink-blue)"/>
          <path d="M5.5 7 L10 10.5 L14.5 7" fill="none" stroke="var(--pale-teal)" stroke-width="1"/>
        </svg>
        <span>sales@marlovistarentals.example</span>
      </li>
    </ul>
  </section>

</main>
</body>
</html>
```